Boutique custom software development company needs new business card

Our nearly 20 year old custom software development company would like to better include the fact that we are now providing Bitcoin services. These new services are B2B include education (how to acquire and securely hold Bitcoin) and integrating Bitcoin payments into existing ecommerce sites or other existing systems. Please keep the card clean and simple. Attached is our current design and some other files. vexalon.example

Target Market(s)

businesses owners interested in long term relationship

Industry/Entity Type

Custom software development and Bitcoin

Contact Information for Business Card

Marcus Ellwood, marcus@vexalon.example, vexalon.example, (888) 555-VEXAL

Font styles to use
Other font styles liked:
• monospace

Requirements
Must have
• double-sided
Nice to have
• clean and simple
Should not have
• physical address

```html
<!DOCTYPE html>
<html lang="en">
<head>
<meta charset="utf-8">
<title>Vexalon Business Card</title>
<link rel="stylesheet" href="https://fonts.googleapis.com/css2?family=Lato:wght@300;400&family=Montserrat:wght@400;500;700;800&display=swap">
<style>
  :root {
    --brand-blue: #4072b9;
    --band-blue: #3d73bb;
    --brand-orange: #ee7623;
    --stripe-yellow: #fbb914;
    --paper: #ffffff;
    --ink: #1b1b1b;
  }
  * { margin: 0; padding: 0; box-sizing: border-box; }
  html, body { width: 800px; height: 1200px; overflow: hidden; background: var(--paper); }
  .canvas { position: relative; width: 800px; height: 1200px; background: var(--paper); font-family: "Montserrat", sans-serif; }
  .top-field { position: absolute; left: 0; top: 0; width: 800px; height: 391px; background: var(--brand-blue); }
  .stripe-orange { position: absolute; left: 0; top: 391px; width: 800px; height: 9px; background: var(--brand-orange); }
  .stripe-yellow { position: absolute; left: 0; top: 400px; width: 800px; height: 9px; background: var(--stripe-yellow); }

  .card { position: absolute; left: 158px; width: 484px; height: 280px; }
  .card-front { top: 57px; background: var(--paper); }
  .card-back { top: 460px; background: var(--brand-blue); }

  .wordmark { position: absolute; left: 0; width: 100%; display: flex; justify-content: center; align-items: center; gap: 7px; font-family: "Montserrat", sans-serif; font-weight: 800; letter-spacing: 0.5px; line-height: 1; }
  .wordmark .mark-square { width: 0.62em; height: 0.62em; background: var(--brand-orange); }
  .card-front .wordmark { top: 74px; font-size: 36px; color: var(--brand-blue); }
  .card-back .wordmark { top: 110px; font-size: 44px; color: var(--paper); }

  .tagline { position: absolute; left: 0; width: 100%; text-align: center; font-family: "Lato", sans-serif; font-weight: 400; letter-spacing: -0.3px; }
  .card-front .tagline { top: 112px; font-size: 13.5px; color: var(--brand-blue); }
  .card-back .tagline { top: 157px; font-size: 15.5px; color: var(--paper); }

  .person { position: absolute; right: 224px; top: 160px; text-align: right; }
  .person-name { font-weight: 700; font-size: 25px; line-height: 1; letter-spacing: 0.3px; }
  .person-name .first { color: var(--brand-orange); }
  .person-name .last { color: var(--brand-blue); }
  .person-email { margin-top: 5px; font-size: 12px; font-weight: 500; color: var(--ink); letter-spacing: 0.6px; }

  .divider { position: absolute; left: 278px; top: 165px; width: 1.5px; height: 37px; background: var(--brand-blue); }

  .contact-list { position: absolute; left: 293px; top: 163px; list-style: none; }
  .contact-list li { display: flex; align-items: center; gap: 8px; height: 23px; font-size: 12.5px; font-weight: 500; color: var(--ink); letter-spacing: 0.6px; }
  .contact-list svg { width: 13px; height: 13px; flex: none; }

  .services-band { position: absolute; left: 0; top: 241px; width: 100%; height: 23px; background: var(--band-blue); display: flex; justify-content: center; align-items: center; gap: 10px; color: var(--paper); font-size: 12.5px; font-weight: 500; letter-spacing: 0.5px; white-space: nowrap; }
  .services-band .dot { width: 4px; height: 4px; border-radius: 50%; background: var(--stripe-yellow); }
</style>
</head>
<body>
<div class="canvas">
  <div class="top-field"></div>
  <div class="stripe-orange"></div>
  <div class="stripe-yellow"></div>

  <section class="card card-front" aria-label="Card front">
    <div class="wordmark"><span class="mark-square"></span><span>VEXALON</span></div>
    <p class="tagline">developer of custom applications</p>

    <div class="person">
      <p class="person-name"><span class="first">Marcus</span> <span class="last">Ellwood</span></p>
      <p class="person-email">marcus@vexalon.example</p>
    </div>

    <div class="divider"></div>

    <ul class="contact-list">
      <li>
        <svg viewBox="0 0 14 14" fill="none" stroke="#4072b9" stroke-width="1.3"><rect x="3.5" y="0.8" width="7" height="12.4" rx="1.2"/><line x1="6" y1="11" x2="8" y2="11"/></svg>
        555.014.0199
      </li>
      <li>
        <svg viewBox="0 0 14 14" fill="none" stroke="#4072b9" stroke-width="1"><circle cx="7" cy="7" r="6"/><ellipse cx="7" cy="7" rx="2.6" ry="6"/><line x1="1" y1="7" x2="13" y2="7"/><path d="M2 4h10M2 10h10"/></svg>
        vexalon.example
      </li>
    </ul>

    <div class="services-band">
      <span>Custom Software</span><span class="dot"></span><span>Bitcoin Payments &amp; Education</span>
    </div>
  </section>

  <section class="card card-back" aria-label="Card back">
    <div class="wordmark"><span class="mark-square"></span><span>VEXALON</span></div>
    <p class="tagline">developer of custom applications</p>
  </section>
</div>
</body>
</html>
```